Vodka Soda brand identity design and label design

New vodka soda (hard seltzer) brand needs a brand identity design and label designs.

The brand name is VELMO

We produce vodka soda packaged in cans. They come in three flavours
- Raspberry and Lime
- Pina Colada
- Black Cherry

We would like to have the designs look similar (same template) but have one difference depending on the fruit flavour.

The final delivered package should contain
- brand identity design guide with a logo, font and colour schemes
- 3 label designs on the same template (label size 8.125 x 5 inches)

Some example designs of similar products are attached to the project.

Target Market(s)

Gender neutral, younger population

Colors
000000

Requirements
Must have
• Bright background and bright eye catching colours.

```html
<!DOCTYPE html>
<html lang="en">
<head>
<meta charset="utf-8">
<title>VELMO Hard Seltzer – Label Range</title>
<link rel="stylesheet" href="https://fonts.googleapis.com/css2?family=Anton&family=Josefin+Sans:wght@700&family=Montserrat:wght@500;700;800&family=Allura&display=swap">
<style>
  :root {
    --canvas-bg: #ececea;
    --label-white: #f7f7f5;
    --ink: #111111;
    --on-colour: #ffffff;
    --pina-yellow: #f1c01c;
    --pina-yellow-deep: #d9a40f;
    --cherry-maroon: #6f1b26;
    --cherry-maroon-deep: #3f0c13;
    --lime-green: #1ec52a;
    --raspberry-red: #d0303a;
    --raspberry-red-deep: #a8181f;
  }
  * { margin: 0; padding: 0; box-sizing: border-box; }
  html, body { width: 1200px; height: 1070px; overflow: hidden; }
  body { background: var(--canvas-bg); }
  .label-range {
    position: relative;
    width: 1200px; height: 1070px;
    display: flex; justify-content: center; align-items: center; gap: 30px;
  }
  .can-label { width: 360px; height: 960px; display: block; box-shadow: 0 6px 18px rgba(0,0,0,.12); }

  .label--pina   { --head: var(--pina-yellow);    --rule: var(--pina-yellow);    --base: var(--pina-yellow);    --base-deep: var(--pina-yellow-deep); }
  .label--cherry { --head: var(--cherry-maroon);  --rule: var(--cherry-maroon);  --base: var(--cherry-maroon);  --base-deep: var(--cherry-maroon-deep); }
  .label--lime   { --head: var(--lime-green);     --rule: var(--lime-green);     --base: var(--raspberry-red);  --base-deep: var(--raspberry-red-deep); }

  .label-body { fill: var(--label-white); }
  .top-band, .base-panel { fill: var(--base); }
  .base-shade { fill: var(--base-deep); opacity: .35; }
  .top-rule { fill: var(--rule); }
  .band-text { font-family: "Montserrat", sans-serif; font-weight: 700; font-size: 14px; fill: var(--on-colour); }
  .brand-name { font-family: "Josefin Sans", sans-serif; font-weight: 700; font-size: 60px; fill: var(--ink); }
  .headline { font-family: "Anton", sans-serif; fill: var(--head); }
  .badge-disc { fill: var(--label-white); stroke: var(--base); stroke-width: 4; }
  .badge-inner { fill: none; stroke: var(--base); stroke-width: 2; }
  .badge-ring-text { font-family: "Montserrat", sans-serif; font-weight: 800; font-size: 12px; fill: var(--base); letter-spacing: 1px; }
  .badge-abv { font-family: "Montserrat", sans-serif; font-weight: 800; font-size: 40px; fill: var(--ink); }
  .badge-abv-label { font-family: "Montserrat", sans-serif; font-weight: 500; font-size: 11px; fill: var(--ink); }
  .hint { font-family: "Allura", cursive; font-size: 40px; fill: var(--on-colour); }
  .flavour { font-family: "Montserrat", sans-serif; font-weight: 800; font-size: 36px; fill: var(--on-colour); }
  .flavour--long { font-size: 29px; }
  .volume { font-family: "Montserrat", sans-serif; font-weight: 500; font-size: 22px; fill: var(--on-colour); }
</style>
</head>
<body>
<main class="label-range">

  <svg class="can-label label--pina" viewBox="0 0 360 960" aria-label="VELMO Hard Seltzer, Pina Colada label">
    <defs>
      <path id="pina-badge-top" d="M132,700 A48,48 0 0 1 228,700"/>
      <path id="pina-badge-bottom" d="M124,700 A56,56 0 0 0 236,700"/>
    </defs>
    <rect class="label-body" width="360" height="960"/>
    <rect class="top-band" width="360" height="58"/>
    <text class="band-text" x="180" y="35" text-anchor="middle">LOREM IPSUM DOLOR SIT  •  LOREM IPSUM</text>
    <rect class="top-rule" y="66" width="360" height="5"/>
    <text class="brand-name" x="180" y="208" text-anchor="middle" textLength="270" lengthAdjust="spacing">VELMO</text>
    <text class="headline" x="32" y="425" font-size="220" textLength="296" lengthAdjust="spacingAndGlyphs">HARD</text>
    <text class="headline" x="10" y="610" font-size="205" textLength="340" lengthAdjust="spacingAndGlyphs">SELTZER</text>
    <path class="base-panel" d="M0,668 C70,650 150,678 230,660 C290,648 330,664 360,656 L360,960 L0,960 Z"/>
    <rect class="base-shade" y="900" width="360" height="60"/>
    <circle class="badge-disc" cx="180" cy="700" r="64"/>
    <circle class="badge-inner" cx="180" cy="700" r="42"/>
    <text class="badge-ring-text" text-anchor="middle"><textPath href="#pina-badge-top" startOffset="50%">100 CALORIES</textPath></text>
    <text class="badge-ring-text" text-anchor="middle"><textPath href="#pina-badge-bottom" startOffset="50%">GLUTEN FREE</textPath></text>
    <text class="badge-abv" x="180" y="708" text-anchor="middle">7%</text>
    <text class="badge-abv-label" x="180" y="724" text-anchor="middle">ALCOHOL</text>
    <text class="hint" x="180" y="825" text-anchor="middle">With a hint of</text>
    <text class="flavour" x="180" y="880" text-anchor="middle" textLength="300" lengthAdjust="spacingAndGlyphs">PINA COLADA</text>
    <text class="volume" x="180" y="938" text-anchor="middle">500ml</text>
  </svg>

  <svg class="can-label label--cherry" viewBox="0 0 360 960" aria-label="VELMO Hard Seltzer, Black Cherry label">
    <defs>
      <path id="cherry-badge-top" d="M132,700 A48,48 0 0 1 228,700"/>
      <path id="cherry-badge-bottom" d="M124,700 A56,56 0 0 0 236,700"/>
    </defs>
    <rect class="label-body" width="360" height="960"/>
    <rect class="top-band" width="360" height="58"/>
    <text class="band-text" x="180" y="35" text-anchor="middle">LOREM IPSUM DOLOR SIT  •  LOREM IPSUM</text>
    <rect class="top-rule" y="66" width="360" height="5"/>
    <text class="brand-name" x="180" y="208" text-anchor="middle" textLength="270" lengthAdjust="spacing">VELMO</text>
    <text class="headline" x="32" y="425" font-size="220" textLength="296" lengthAdjust="spacingAndGlyphs">HARD</text>
    <text class="headline" x="10" y="610" font-size="205" textLength="340" lengthAdjust="spacingAndGlyphs">SELTZER</text>
    <path class="base-panel" d="M0,668 C70,650 150,678 230,660 C290,648 330,664 360,656 L360,960 L0,960 Z"/>
    <rect class="base-shade" y="900" width="360" height="60"/>
    <circle class="badge-disc" cx="180" cy="700" r="64"/>
    <circle class="badge-inner" cx="180" cy="700" r="42"/>
    <text class="badge-ring-text" text-anchor="middle"><textPath href="#cherry-badge-top" startOffset="50%">100 CALORIES</textPath></text>
    <text class="badge-ring-text" text-anchor="middle"><textPath href="#cherry-badge-bottom" startOffset="50%">GLUTEN FREE</textPath></text>
    <text class="badge-abv" x="180" y="708" text-anchor="middle">7%</text>
    <text class="badge-abv-label" x="180" y="724" text-anchor="middle">ALCOHOL</text>
    <text class="hint" x="180" y="825" text-anchor="middle">With a hint of</text>
    <text class="flavour" x="180" y="880" text-anchor="middle" textLength="310" lengthAdjust="spacingAndGlyphs">BLACK CHERRY</text>
    <text class="volume" x="180" y="938" text-anchor="middle">500ml</text>
  </svg>

  <svg class="can-label label--lime" viewBox="0 0 360 960" aria-label="VELMO Hard Seltzer, Raspberry and Lime label">
    <defs>
      <path id="lime-badge-top" d="M132,700 A48,48 0 0 1 228,700"/>
      <path id="lime-badge-bottom" d="M124,700 A56,56 0 0 0 236,700"/>
    </defs>
    <rect class="label-body" width="360" height="960"/>
    <rect class="top-band" width="360" height="58"/>
    <text class="band-text" x="180" y="35" text-anchor="middle">LOREM IPSUM DOLOR SIT  •  LOREM IPSUM</text>
    <rect class="top-rule" y="66" width="360" height="5"/>
    <text class="brand-name" x="180" y="208" text-anchor="middle" textLength="270" lengthAdjust="spacing">VELMO</text>
    <text class="headline" x="32" y="425" font-size="220" textLength="296" lengthAdjust="spacingAndGlyphs">HARD</text>
    <text class="headline" x="10" y="610" font-size="205" textLength="340" lengthAdjust="spacingAndGlyphs">SELTZER</text>
    <path class="base-panel" d="M0,668 C70,650 150,678 230,660 C290,648 330,664 360,656 L360,960 L0,960 Z"/>
    <rect class="base-shade" y="900" width="360" height="60"/>
    <circle class="badge-disc" cx="180" cy="700" r="64"/>
    <circle class="badge-inner" cx="180" cy="700" r="42"/>
    <text class="badge-ring-text" text-anchor="middle"><textPath href="#lime-badge-top" startOffset="50%">100 CALORIES</textPath></text>
    <text class="badge-ring-text" text-anchor="middle"><textPath href="#lime-badge-bottom" startOffset="50%">GLUTEN FREE</textPath></text>
    <text class="badge-abv" x="180" y="708" text-anchor="middle">7%</text>
    <text class="badge-abv-label" x="180" y="724" text-anchor="middle">ALCOHOL</text>
    <text class="hint" x="180" y="825" text-anchor="middle">With a hint of</text>
    <text class="flavour flavour--long" x="180" y="877" text-anchor="middle" textLength="320" lengthAdjust="spacingAndGlyphs">RASPBERRY &amp; LIME</text>
    <text class="volume" x="180" y="938" text-anchor="middle">500ml</text>
  </svg>

</main>
</body>
</html>
```